Small Cafe, hidden in an office building, needs a menu layout, to help it stand out.

So we need a menu layout for a very small cafe that can work for both customers in the cafe, as well as being handed out to local businesses. Boring, I know. Well here's some things to give direction and make it more fun.
1. It's an American Korean hybrid. American sandwiches and subs but also Korean dishes including Korean Style Chicken Wings. Her wings are amazing! No, even better then what you just thought.
2. I'm American born, & my wife who runs the cafe, was born in Seoul Korea. I had been toying with the thought of incorporating the Korean flag into a logo. I will attach the images to try and make it clearer.
3. It's called "Harbor Nook Cafe" no, we didn't name it, but what can you do eh? Anywho, the acronym for it is HNC. So we have been using the line, "The main ingredient in great food is the HNC." That doesn't have to stay but I dunno, kinda clever.
4. It has to stay professional kinda because we are in an office building, however my wife has a good sense of humor and laughs a lot. She tries to make it fun and not stuffy by joking around with the customers. They all love her smile and upbeat nature.
5. We are located in College Park MD close to Ashgrove Valley University in an office building, but we both wish we were out in West Virginia in the country.
6. One of her main dishes as far a popularity, is her Korean chicken wings and it just so happens we both love Roosters. Long story... and we do espresso... I'm imagining a coffee drinking rooster with his eyes bugged out on his caffeine buzz. Maybe it's just the fear of the fryer...
7. I thought today, "It sucks we're cooped up in the back of the lobby." ha... ahhhh... I need sleep.
8. I'm including a place holder I made for the website back when we were thinking of calling it PelicanBay Chicken. The Korean flag with it's meanings that are associated with my drawing of a possible logo... Did I mention I need a log designed too? Huh... Ok, well I attached the logo I was thinking about ripping off as the basis of that Idea. I'm not sold on it. It's just something my pea sized brain came up with. I have also attached a picture of my wife at the cafe that way you can get a vibe of her and the place. The menu items. Lastly a picture of a Rooster that I just simply love. I adjusted him in Photoshop and just love the color. Not sure about him making an appearance on the menu... just kinda showing him off I guess. I said I needed sleep right?...
Thanks for reading. Rule the roost!
-Corwin

```html
<!DOCTYPE html>
<html lang="en">
<head>
<meta charset="utf-8">
<title>Harbor Nook Cafe – Menu</title>
<link rel="stylesheet" href="https://fonts.googleapis.com/css2?family=Open+Sans:wght@400;700&family=Yellowtail&display=swap">
<style>
  :root {
    --ink: #000000;
    --paper: #ffffff;
    --fold: #bfbfbf;
    --red: #e0191c;
    --yellow: #f2e627;
    --cyan: #2fd3e8;
    --rooster: #ff5a0a;
    --tracks: #f5e600;
  }
  * { margin: 0; padding: 0; box-sizing: border-box; }
  html, body { width: 1200px; height: 856px; overflow: hidden; background: var(--ink); }
  .menu {
    position: relative;
    width: 1200px;
    height: 856px;
    overflow: hidden;
    background: var(--ink);
    color: var(--paper);
    font-family: "Open Sans", Arial, sans-serif;
    font-size: 16px;
    line-height: 20px;
    text-align: center;
  }
  .fold {
    position: absolute;
    top: 0;
    width: 0;
    height: 856px;
    border-left: 1.5px dashed var(--fold);
  }
  .fold--first { left: 393px; }
  .fold--second { left: 785px; }

  .panel { position: absolute; top: 0; height: 856px; }
  .panel--korean { left: 0; width: 393px; }
  .panel--breakfast { left: 393px; width: 392px; }
  .panel--cover { left: 785px; width: 415px; }

  .section-title {
    font-family: "Yellowtail", cursive;
    font-weight: 400;
    font-size: 27px;
    line-height: 30px;
  }
  .section-title--korean { color: var(--red); margin: 40px 0 19px; }
  .section-title--breakfast { color: var(--yellow); margin: 38px 0 17px; }
  .section-title--drinks { color: var(--cyan); margin: 0 0 1px; }

  .dish { margin: 0 auto 40px; width: 285px; font-size: 17px; line-height: 20px; }
  .dish__name { font-size: 17px; font-weight: 700; }
  .dish__desc { display: block; }

  .breakfast-list { list-style: none; }
  .breakfast-item { margin-bottom: 19px; }
  .breakfast-item__name { font-weight: 700; display: block; }

  .drinks-list { list-style: none; line-height: 19.5px; }

  .rooster {
    position: absolute;
    left: 48px;
    top: 622px;
    width: 215px;
    height: 188px;
    background: var(--rooster);
    border-radius: 40% 45% 10% 30%;
  }
  .tracks {
    position: absolute;
    left: 215px;
    top: 772px;
    width: 160px;
    height: 84px;
    background: linear-gradient(100deg, rgba(245,230,0,0.55), rgba(245,230,0,0.25));
    border-radius: 24px 24px 0 0;
  }

  .tagline {
    position: absolute;
    left: 0;
    top: 18px;
    width: 415px;
    height: 120px;
    overflow: visible;
  }
  .tagline text {
    font-family: "Yellowtail", cursive;
    font-size: 24px;
    fill: var(--red);
  }
  .brand {
    position: absolute;
    top: 140px;
    left: 0;
    width: 415px;
    font-family: "Open Sans", Arial, sans-serif;
    font-weight: 400;
    font-size: 80px;
    line-height: 108px;
    color: var(--paper);
  }
  .phone {
    position: absolute;
    top: 546px;
    left: 0;
    width: 400px;
    font-weight: 700;
    font-size: 35px;
    line-height: 44px;
  }
  .details {
    position: absolute;
    top: 632px;
    left: 0;
    width: 400px;
    font-style: normal;
    font-size: 17px;
    line-height: 21px;
  }
  .details__label { font-weight: 700; }
  .details__block { margin-bottom: 22px; }
</style>
</head>
<body>
<main class="menu">
  <div class="fold fold--first"></div>
  <div class="fold fold--second"></div>

  <section class="panel panel--korean">
    <h2 class="section-title section-title--korean">Korean Favorites</h2>
    <article class="dish">
      <h3 class="dish__name">Chicken Wings (8)</h3>
      <p class="dish__desc">Korean Chicken Wings are juicy, spicy, &amp; sweet, &amp; impossible to just eat one. Made with Mirae's homemade sauce!</p>
      <p class="dish__price">7.99</p>
    </article>
    <article class="dish">
      <h3 class="dish__name">Bibimbap</h3>
      <p class="dish__desc">Multiple mixed Vegetables, Rice, a Fried Egg &amp; Chili Pepper Paste.</p>
      <p class="dish__price">9.99</p>
    </article>
    <article class="dish">
      <h3 class="dish__name">Beef BBQ Bulgogi</h3>
      <p class="dish__desc">Sliced marinated Beef with Onion, Carrot, Zucchini, Green &amp; Red peppers.</p>
      <p class="dish__price">9.99</p>
    </article>
    <article class="dish">
      <h3 class="dish__name">Spicy Pork Bulgogi</h3>
      <p class="dish__desc">Daeji Bulgogi is sliced marinated Pork, cooked with Vegetables &amp; served on Rice.</p>
      <p class="dish__price">9.99</p>
    </article>
    <div class="rooster" role="img" aria-label="Orange rooster silhouette strutting"></div>
  </section>

  <div class="tracks" role="img" aria-label="Trail of yellow rooster footprints"></div>

  <section class="panel panel--breakfast">
    <h2 class="section-title section-title--breakfast">Breakfast</h2>
    <ul class="breakfast-list">
      <li class="breakfast-item"><span class="breakfast-item__name">Egg &amp; Cheese Sandwich</span>2.99</li>
      <li class="breakfast-item"><span class="breakfast-item__name">Sausage, Egg &amp; Cheese Sandwich</span>3.59</li>
      <li class="breakfast-item"><span class="breakfast-item__name">Bacon, Egg &amp; Cheese Sandwich</span>3.59</li>
      <li class="breakfast-item"><span class="breakfast-item__name">Bagel &amp; Cream Cheese</span>1.99</li>
      <li class="breakfast-item"><span class="breakfast-item__name">Veggie Omelet</span>4.49</li>
      <li class="breakfast-item"><span class="breakfast-item__name">Western Omelet</span>5.29</li>
      <li class="breakfast-item"><span class="breakfast-item__name">Classic Platter</span>4.49</li>
      <li class="breakfast-item"><span class="breakfast-item__name">French Toast Platter</span>4.49</li>
      <li class="breakfast-item"><span class="breakfast-item__name">Home Fries</span>2.25</li>
    </ul>
    <h2 class="section-title section-title--drinks">Drinks</h2>
    <ul class="drinks-list">
      <li>Espresso</li>
      <li>Americano</li>
      <li>Cappuccino</li>
      <li>Cafe Latte</li>
      <li>Cafe Mocha</li>
      <li>Caramel Macchiato</li>
      <li>Chai Tea Latte</li>
      <li>Tea</li>
    </ul>
  </section>

  <section class="panel panel--cover">
    <svg class="tagline" viewBox="0 0 415 120" aria-label="The main ingredient in great food is HNC">
      <defs>
        <path id="tagline-arc" d="M 18 112 Q 200 -62 392 112"/>
      </defs>
      <text><textPath href="#tagline-arc" startOffset="50%" text-anchor="middle" textLength="380" lengthAdjust="spacingAndGlyphs">The main ingredient in great food is HNC</textPath></text>
    </svg>
    <h1 class="brand">Harbor<br>Nook<br>Cafe</h1>
    <p class="phone">301-555-0148</p>
    <address class="details">
      <p class="details__block"><span class="details__label">Hours</span><br>Monday - Friday<br>7:30am - 4:30pm</p>
      <p class="details__block">4120 Fenwick Ave,<br>College Park,<br>MD&nbsp; 20740</p>
      <p class="details__block">www.harbornookcafe.net</p>
    </address>
  </section>
</main>
</body>
</html>
```